Harbourline Blinds & Shutters

It Needs to look classy as my target is the upper end of the blind market
I need a Logo design on front and description on back of what i do:
- Roller Blinds
- Vertical Blinds
- Venetian Blinds
- Plantation Shutters
- Aluminum External Shutters
and contact details
Gavin
0418527306
and
Terry
0421690358
Updates
Hi Guys,
Sorry for the no feedback but i was waiting on my logo design. But its done now i have uploaded it. so if you could take a look and send through some designs
Reason: my logo was just finished an i just uploaded it today really dont understand why my deadline has been rached foe my bizcards as it states no deadline. But please extend
Target Market(s)
People that live on the coast and are looking for classy good quality blinds and shutters
Font styles to use
Other font styles liked:
- Copperplate Gothic,open to suggestion
Look and feel
Each slider illustrates characteristics of the customer's brand and the style your logo design should communicate.

```html
<!DOCTYPE html>
<html lang="en">
<head>
<meta charset="utf-8">
<title>Harbourline Blinds &amp; Shutters – Business Card</title>
<link rel="stylesheet" href="https://fonts.googleapis.com/css2?family=Cinzel:wght@400;700&family=Libre+Baskerville:wght@400;700&display=swap">
<style>
  :root {
    --backdrop: #e9e9e7;
    --cream-light: #fff9a8;
    --cream-deep: #f7ec86;
    --cocoa: #4a2810;
    --cocoa-dark: #3c1f0b;
    --cocoa-ghost: rgba(30, 14, 4, 0.35);
    --ink: #3d210c;
    --silver: #9c9a94;
    --gold: #e2c27a;
    --card-shadow: 0 10px 24px rgba(0, 0, 0, 0.18);
  }
  * { box-sizing: border-box; margin: 0; padding: 0; }
  html, body {
    width: 1200px;
    height: 857px;
    overflow: hidden;
    background: var(--backdrop);
  }
  .sheet {
    position: relative;
    width: 1200px;
    height: 857px;
    display: flex;
    align-items: center;
    justify-content: center;
    gap: 60px;
  }
  .card {
    position: relative;
    width: 500px;
    height: 286px;
    border-radius: 26px;
    overflow: hidden;
    box-shadow: var(--card-shadow);
  }

  /* Front */
  .card--front {
    background: linear-gradient(160deg, var(--cream-light), var(--cream-deep));
    display: flex;
    flex-direction: column;
    align-items: center;
    justify-content: center;
  }
  .brand-dot {
    width: 78px;
    height: 78px;
    margin-bottom: 14px;
  }
  .brand-name {
    font-family: "Cinzel", serif;
    font-weight: 700;
    font-size: 42px;
    letter-spacing: 1px;
    color: var(--ink);
    line-height: 1;
  }
  .brand-tagline {
    font-family: "Cinzel", serif;
    font-weight: 400;
    font-size: 15px;
    letter-spacing: 2px;
    color: var(--silver);
    margin-top: 6px;
  }

  /* Back */
  .card--back {
    background: linear-gradient(160deg, var(--cocoa), var(--cocoa-dark));
    text-align: center;
    padding-top: 30px;
  }
  .contacts {
    font-family: "Libre Baskerville", serif;
    font-size: 13px;
    line-height: 1.55;
    color: var(--gold);
    position: relative;
    z-index: 1;
  }
  .contacts strong { font-weight: 700; letter-spacing: 1px; }
  .ghost-name {
    position: absolute;
    left: 0;
    right: 0;
    top: 70px;
    font-family: "Cinzel", serif;
    font-weight: 700;
    font-size: 62px;
    color: var(--cocoa-ghost);
    letter-spacing: 2px;
    line-height: 1;
  }
  .ghost-tagline {
    position: absolute;
    left: 0;
    right: 0;
    top: 140px;
    font-family: "Cinzel", serif;
    font-size: 24px;
    letter-spacing: 3px;
    color: var(--cocoa-ghost);
  }
  .services {
    position: absolute;
    left: 0;
    right: 0;
    top: 180px;
    font-family: "Libre Baskerville", serif;
    font-size: 13px;
    line-height: 1.5;
    color: var(--gold);
    list-style: none;
  }
  .services li { display: inline; }
  .services li + li::before {
    content: "";
    display: inline-block;
    width: 6px;
    height: 6px;
    margin: 0 7px 2px;
    background: var(--gold);
    opacity: 0.6;
  }
  .services .row { display: block; }
  .services .row li:first-child::before { content: none; }
</style>
</head>
<body>
  <main class="sheet">
    <section class="card card--front" aria-label="Business card front">
      <svg class="brand-dot" viewBox="0 0 78 78" aria-hidden="true">
        <circle cx="39" cy="39" r="37" fill="#4a2810"/>
      </svg>
      <h1 class="brand-name">HARBOURLINE</h1>
      <p class="brand-tagline">BLINDS &amp; SHUTTERS</p>
    </section>

    <section class="card card--back" aria-label="Business card back">
      <p class="contacts">
        <strong>GAVIN</strong>-0418527306<br>
        <strong>TERRY</strong>-0421690358
      </p>
      <div class="ghost-name" aria-hidden="true">HARBOURLINE</div>
      <div class="ghost-tagline" aria-hidden="true">BLINDS &amp; SHUTTERS</div>
      <div class="services">
        <ul class="row">
          <li>Roller Blinds</li><li>Vertical Blinds</li><li>Venetian Blinds</li>
        </ul>
        <ul class="row">
          <li>Plantation Shutters</li><li>Aluminum External Shutters</li>
        </ul>
      </div>
    </section>
  </main>
</body>
</html>
```